Smartphone Social app needs an app design team

We need a smartphone app design for new company based in the NYC area called "qLoom Ventures, Inc." We are a smartphone application development company focused on utilizing uTether technologies to facilitate meeting and socializing with people that are in proximity to you.
Our first app is called qLoomtalk.net which helps people that are in physical proximity break the ice and encourages mingling with people at a party or an event.
The final design should communicate a sense of bringing social networking back to being human and meeting people in the real world.
Should be fun, contemporary, and communicate a sense of local area networking (physical world).
The scope of this design mockups that we are looking for would to design a people bingo like game for the phone facilitating meeting and breaking the ice with people in proximity with you.
When you’re ready to play, the game would provide each participant in proximity a bingo card with peoples profile characteristics and traits printed in each box. The guests have 30 minutes to mingle, introducing themselves, and find people who match the traits on the card. They must put the person’s profile picture in the corresponding box.
The first person to fill five boxes across or down yells BINGO! and that person wins the game.
Updates

Please see updated brief, describing more clearly the people bingo game concept. Thanks for your interest in designing this feature for our social app.

Reason: Changed and added more clarity to brief

Hi designers, I Updated the project brief to clarify Bingo game concept. Please add designs to simulate a bingo game concept. I know the size of the screen doesn't facilitate a bingo game, but think of way to get the same user experience with a small screen. Thanks, Dale

To all Designers, I have uploaded the new Logo for qLoomtalk and would like everyone to use the attached logos and assimilate the colors in the design. Thanks very much, Dale K.

Reason: Further clarification on app posted a few days ago.

Target Market(s)

Young adults 21-30
- College Students
- Young business professional

Industry/Entity Type

It Company

Font styles to use
Sans Serif

Requirements
Must have
• Ability to host an event
Message people in proximity to you to join the fun and download app
Build profile from GV and Trelmo
See profile and compatible traits and or dislikes (like went to same school, etc.)
Develop UX for a people bingo like game to get people to mingle and learn about each other

```html
<!DOCTYPE html>
<html lang="en">
<head>
<meta charset="utf-8">
<title>Bingo – qLoomtalk app screens</title>
<link rel="stylesheet" href="https://fonts.googleapis.com/css2?family=Kaushan+Script&family=Questrial&display=swap">
<style>
:root{
  --page:#eef0f1;
  --green-light:#c6ec86;
  --green-mid:#9fd64e;
  --green-deep:#6aa21f;
  --green-header:#5f9a1c;
  --olive:#4c6a1e;
  --olive-dark:#3f5a18;
  --ink:#1e1e1e;
  --white:#ffffff;
  --teal:#16b9a2;
  --yellow:#f6bd16;
  --red:#ec1c24;
  --blue:#1497c6;
  --orange:#f08a1c;
  --cell-dark:#2a2a2a;
  --photo:#a3897a;
  --photo-alt:#7c6a60;
}
*{box-sizing:border-box;margin:0;padding:0}
html,body{width:1200px;height:576px;overflow:hidden;background:var(--page)}
body{position:relative;font-family:"Questrial",sans-serif;color:var(--ink)}
.screen{position:absolute;top:125px;width:205px;height:362px;transform:scale(.816);transform-origin:0 0;overflow:hidden;background:var(--green-light);border:1px solid #222}
.screen--splash{left:50px}.screen--home{left:284px}.screen--search{left:516px}.screen--game{left:750px}.screen--winner{left:984px}
.status-bar{height:13px;background:#0c0c0c;color:#fff;font-size:7px;display:flex;justify-content:space-between;align-items:center;padding:0 6px}
.app-title{font-family:"Kaushan Script",cursive;color:var(--white);font-size:19px}
.app-header{height:42px;background:var(--green-header);display:flex;align-items:center;padding-left:8px}
.app-header .app-title{flex:1}
.header-btn{width:30px;height:42px;display:flex;align-items:center;justify-content:center;border-left:1px solid rgba(0,0,0,.15)}
.header-btn svg{width:15px;height:15px;fill:var(--white)}
.glow{background:radial-gradient(circle at 50% 45%,#d7f5a2 0%,var(--green-light) 40%,var(--green-mid) 100%)}
.avatar{border-radius:50%;background:radial-gradient(circle at 50% 40%,var(--photo) 0%,var(--photo-alt) 100%);border:3px solid var(--olive-dark)}
/* splash */
.splash-body{height:349px;display:flex;flex-direction:column;align-items:center;justify-content:center;background:radial-gradient(circle at 50% 45%,#b8ea6d 0%,var(--green-mid) 70%,#8fcb3b 100%)}
.splash-title{font-family:"Kaushan Script",cursive;font-size:46px;color:var(--ink);margin-top:-20px}
.splash-by{font-size:9px;margin-top:22px}
.brand{display:flex;align-items:center;gap:4px;margin-top:4px;font-size:11px;color:var(--orange)}
.brand-dot{width:14px;height:14px;border-radius:50%;background:var(--orange)}
/* home */
.profile{height:100px;display:flex;align-items:center;justify-content:center}
.profile .avatar{width:66px;height:66px}
.profile-bar{height:40px;background:var(--olive);color:var(--white);display:flex;align-items:center;justify-content:space-between;padding:0 8px}
.profile-name{font-size:13px;font-weight:700}
.profile-place{font-size:8px;opacity:.85}
.tiles{background:var(--white);display:grid;grid-template-columns:1fr 1fr;gap:6px;padding:6px;height:167px}
.tile{display:flex;flex-direction:column;align-items:center;justify-content:flex-end;color:var(--white);font-size:9px;padding-bottom:5px}
.tile svg{width:40px;height:34px;fill:var(--white);margin-bottom:6px}
.tile--play{background:var(--teal)}.tile--how{background:var(--yellow)}.tile--scores{background:var(--red)}.tile--share{background:var(--blue)}
/* search */
.search-body{position:relative;height:265px}
.refresh{position:absolute;left:5px;top:5px;width:22px;height:22px;background:#e4f6c8;display:flex;align-items:center;justify-content:center}
.search-center{position:absolute;top:70px;width:100%;text-align:center;font-size:9px;font-weight:700}
.search-center svg{display:block;margin:10px auto 4px;width:70px;height:54px}
.note{position:absolute;bottom:4px;left:6px;right:6px;font-size:4.5px;color:#333}
.people-strip{height:42px;background:var(--green-deep);position:relative;display:flex;align-items:center;justify-content:center;gap:5px;padding-top:8px}
.strip-label{position:absolute;top:1px;width:100%;text-align:center;font-size:5px;color:var(--white)}
.people-strip .avatar{width:24px;height:24px;border:2px solid #fff}
.arrow{color:var(--white);font-size:13px}
/* game */
.timer{height:12px;background:#bfe680;display:flex;justify-content:space-between;align-items:center;padding:0 4px;font-size:6px}
.digits{display:flex;gap:1px}
.digits span{background:#111;color:#fff;width:8px;height:9px;font-size:6px;display:flex;align-items:center;justify-content:center}
.card{margin:6px 5px 0;display:grid;grid-template-columns:repeat(5,1fr);gap:1px;background:#999}
.card-letter{background:#eee;text-align:center;font-size:15px;font-weight:700;height:20px;line-height:20px}
.cell{height:36px;padding:2px;font-size:4px;line-height:1.1;display:flex;flex-direction:column;justify-content:space-between;background:var(--white)}
.cell--dark{background:var(--cell-dark);color:#fff}
.cell span+span{border-top:1px solid #888;padding-top:2px}
.cell--photo{background:radial-gradient(circle at 50% 40%,var(--photo) 0%,var(--photo-alt) 100%)}
.game-strip{position:absolute;bottom:0;width:100%;height:46px;background:var(--green-deep);display:flex;align-items:center;justify-content:center;gap:4px}
.person{display:flex;flex-direction:column;align-items:center;font-size:4.5px;color:#fff}
.person .avatar{width:22px;height:22px;border:2px solid #fff;margin-bottom:1px}
/* winner */
.winner-body{height:307px;text-align:center;padding-top:50px}
.winner-label{font-size:17px;font-weight:700}
.winner-body .avatar{width:70px;height:70px;margin:10px auto 8px}
.winner-name{font-size:12px;font-weight:700}
</style>
</head>
<body>

<section class="screen screen--splash">
  <div class="status-bar"><span>●●●○○ VOLT</span><span>4:21 PM</span><span>22%</span></div>
  <div class="splash-body">
    <div class="splash-title">Bingo</div>
    <div class="splash-by">by</div>
    <div class="brand"><span class="brand-dot"></span><span>qLoomtalk</span></div>
  </div>
</section>

<section class="screen screen--home">
  <div class="status-bar"><span>●●●○○ VOLT</span><span>4:21 PM</span><span>22%</span></div>
  <header class="app-header"><span class="app-title">Bingo</span>
    <span class="header-btn"><svg viewBox="0 0 20 20"><path d="M10 6a4 4 0 100 8 4 4 0 000-8zm8 5V9l-2.3-.5-.6-1.4 1.3-2-1.5-1.5-2 1.3-1.4-.6L11 2H9l-.5 2.3-1.4.6-2-1.3L3.6 5.1l1.3 2-.6 1.4L2 9v2l2.3.5.6 1.4-1.3 2 1.5 1.5 2-1.3 1.4.6L9 18h2l.5-2.3 1.4-.6 2 1.3 1.5-1.5-1.3-2 .6-1.4z"/></svg></span>
  </header>
  <div class="profile glow"><div class="avatar" role="img" aria-label="Profile photo of the player"></div></div>
  <div class="profile-bar"><div><div class="profile-name">Owen Hartley</div><div class="profile-place">California</div></div>
    <svg width="16" height="16" viewBox="0 0 20 20" fill="#fff"><path d="M3 14l9-9 3 3-9 9H3zM13 4l2-2 3 3-2 2z"/></svg></div>
  <nav class="tiles">
    <div class="tile tile--play"><svg viewBox="0 0 40 30"><path d="M10 4h20a9 9 0 019 11l-2 9a4 4 0 01-7 1l-3-4H13l-3 4a4 4 0 01-7-1l-2-9A9 9 0 0110 4z"/></svg>Play</div>
    <div class="tile tile--how"><svg viewBox="0 0 40 34"><circle cx="22" cy="5" r="4"/><path d="M17 12h9l-5 18h5l-1 3h-10l5-18h-4z"/></svg>How to Play</div>
    <div class="tile tile--scores"><svg viewBox="0 0 40 34"><path d="M10 2h20v10a10 10 0 01-20 0zM4 4h6v4H8a3 3 0 006 4v2A6 6 0 014 8zM36 4h-6v4h2a3 3 0 01-6 4v2a6 6 0 0010-6zM17 21h6v6h-6zM12 28h16v4H12z"/></svg>High Scores</div>
    <div class="tile tile--share"><svg viewBox="0 0 40 34"><circle cx="28" cy="7" r="6"/><circle cx="10" cy="17" r="6"/><circle cx="28" cy="27" r="6"/><path d="M10 16l18-10 1 2-18 10zM11 16l18 10-1 2-18-10z"/></svg>Share</div>
  </nav>
</section>

<section class="screen screen--search">
  <div class="status-bar"><span>●●●○○ VOLT</span><span>4:21 PM</span><span>22%</span></div>
  <header class="app-header"><span class="app-title">Bingo</span>
    <span class="header-btn"><svg viewBox="0 0 20 20"><path d="M10 2l9 8h-3v8h-4v-5H8v5H4v-8H1z"/></svg></span>
    <span class="header-btn"><svg viewBox="0 0 20 20"><path d="M10 6a4 4 0 100 8 4 4 0 000-8zm8 5V9l-2.3-.5-.6-1.4 1.3-2-1.5-1.5-2 1.3-1.4-.6L11 2H9l-.5 2.3-1.4.6-2-1.3L3.6 5.1l1.3 2-.6 1.4L2 9v2l2.3.5.6 1.4-1.3 2 1.5 1.5 2-1.3 1.4.6L9 18h2l.5-2.3 1.4-.6 2 1.3 1.5-1.5-1.3-2 .6-1.4z"/></svg></span>
  </header>
  <div class="search-body glow">
    <div class="refresh"><svg width="14" height="14" viewBox="0 0 20 20" fill="none" stroke="#4d8a16" stroke-width="2.5"><path d="M16 10a6 6 0 11-2-4.5"/><path d="M15 2v4h-4"/></svg></div>
    <div class="search-center">Searching...
      <svg viewBox="0 0 70 54" fill="none" stroke="#111" stroke-width="4" stroke-linecap="round"><path d="M35 18L27 52M35 18l8 34M30 38h10M29 45h12"/><circle cx="35" cy="15" r="4" fill="#111" stroke="none"/><path d="M25 6a14 14 0 000 18M45 6a14 14 0 010 18M17 1a22 22 0 000 28M53 1a22 22 0 010 28"/></svg>
      17/25 found</div>
    <p class="note"><b>Note:</b> As soon as 25 people in proximity are discovered the game will automatically start.</p>
  </div>
  <div class="people-strip"><span class="strip-label">Found People</span><span class="arrow">‹</span>
    <div class="avatar" role="img" aria-label="Found person photo"></div><div class="avatar" role="img" aria-label="Found person photo"></div><div class="avatar" role="img" aria-label="Found person photo"></div><div class="avatar" role="img" aria-label="Found person photo"></div><div class="avatar" role="img" aria-label="Found person photo"></div><div class="avatar" role="img" aria-label="Found person photo"></div><span class="arrow">›</span></div>
</section>

<section class="screen screen--game">
  <div class="status-bar"><span>●●●○○ VOLT</span><span>4:21 PM</span><span>22%</span></div>
  <header class="app-header"><span class="app-title">Bingo</span>
    <span class="header-btn"><svg viewBox="0 0 20 20"><path d="M10 2l9 8h-3v8h-4v-5H8v5H4v-8H1z"/></svg></span>
    <span class="header-btn"><svg viewBox="0 0 20 20"><circle cx="10" cy="10" r="9"/><text x="10" y="14.5" font-size="13" text-anchor="middle" fill="#5f9a1c" font-family="sans-serif" font-weight="700">?</text></svg></span>
    <span class="header-btn"><svg viewBox="0 0 20 20"><path d="M10 6a4 4 0 100 8 4 4 0 000-8zm8 5V9l-2.3-.5-.6-1.4 1.3-2-1.5-1.5-2 1.3-1.4-.6L11 2H9l-.5 2.3-1.4.6-2-1.3L3.6 5.1l1.3 2-.6 1.4L2 9v2l2.3.5.6 1.4-1.3 2 1.5 1.5 2-1.3 1.4.6L9 18h2l.5-2.3 1.4-.6 2 1.3 1.5-1.5-1.3-2 .6-1.4z"/></svg></span>
  </header>
  <div class="timer"><span>Time Remaining</span><span class="digits"><span>1</span><span>8</span><span>2</span><span>3</span></span></div>
  <div class="card">
    <div class="card-letter">B</div><div class="card-letter">I</div><div class="card-letter">N</div><div class="card-letter">G</div><div class="card-letter">O</div>
    <div class="cell cell--dark"><span>This is a Characteristic given</span><span>This is a trait given</span></div>
    <div class="cell cell--photo" role="img" aria-label="Matched person photo"></div>
    <div class="cell cell--dark"><span>This is a Characteristic given</span><span>This is a trait given</span></div>
    <div class="cell"><span>This is a Characteristic given</span><span>This is a trait given</span></div>
    <div class="cell cell--dark"><span>This is a Characteristic given</span><span>This is a trait given</span></div>
    <div class="cell"><span>This is a Characteristic given</span><span>This is a trait given</span></div>
    <div class="cell cell--dark"><span>This is a Characteristic given</span><span>This is a trait given</span></div>
    <div class="cell"><span>This is a Characteristic given</span><span>This is a trait given</span></div>
    <div class="cell cell--dark"><span>This is a Characteristic given</span><span>This is a trait given</span></div>
    <div class="cell"><span>This is a Characteristic given</span><span>This is a trait given</span></div>
    <div class="cell cell--dark"><span>This is a Characteristic given</span><span>This is a trait given</span></div>
    <div class="cell cell--photo" role="img" aria-label="Matched person photo"></div>
    <div class="cell cell--photo" role="img" aria-label="Matched person photo"></div>
    <div class="cell cell--photo" role="img" aria-label="Matched person photo"></div>
    <div class="cell cell--dark"><span>This is a Characteristic given</span><span>This is a trait given</span></div>
    <div class="cell"><span>This is a Characteristic given</span><span>This is a trait given</span></div>
    <div class="cell cell--photo" role="img" aria-label="Matched person photo"></div>
    <div class="cell"><span>This is a Characteristic given</span><span>This is a trait given</span></div>
    <div class="cell cell--dark"><span>This is a Characteristic given</span><span>This is a trait given</span></div>
    <div class="cell"><span>This is a Characteristic given</span><span>This is a trait given</span></div>
    <div class="cell cell--dark"><span>This is a Characteristic given</span><span>This is a trait given</span></div>
    <div class="cell"><span>This is a Characteristic given</span><span>This is a trait given</span></div>
    <div class="cell cell--dark"><span>This is a Characteristic given</span><span>This is a trait given</span></div>
    <div class="cell"><span>This is a Characteristic given</span><span>This is a trait given</span></div>
    <div class="cell cell--dark"><span>This is a Characteristic given</span><span>This is a trait given</span></div>
  </div>
  <div class="game-strip"><span class="arrow">‹</span>
    <div class="person"><div class="avatar" role="img" aria-label="Player photo"></div>Mark</div>
    <div class="person"><div class="avatar" role="img" aria-label="Player photo"></div>Lisa</div>
    <div class="person"><div class="avatar" role="img" aria-label="Player photo"></div>Jennifer</div>
    <div class="person"><div class="avatar" role="img" aria-label="Player photo"></div>Ilana</div>
    <div class="person"><div class="avatar" role="img" aria-label="Player photo"></div>Tom</div>
    <div class="person"><div class="avatar" role="img" aria-label="Player photo"></div>Sheila</div>
    <span class="arrow">›</span></div>
</section>

<section class="screen screen--winner">
  <div class="status-bar"><span>●●●○○ VOLT</span><span>4:21 PM</span><span>22%</span></div>
  <header class="app-header"><span class="app-title">Bingo</span>
    <span class="header-btn"><svg viewBox="0 0 20 20"><path d="M10 6a4 4 0 100 8 4 4 0 000-8zm8 5V9l-2.3-.5-.6-1.4 1.3-2-1.5-1.5-2 1.3-1.4-.6L11 2H9l-.5 2.3-1.4.6-2-1.3L3.6 5.1l1.3 2-.6 1.4L2 9v2l2.3.5.6 1.4-1.3 2 1.5 1.5 2-1.3 1.4.6L9 18h2l.5-2.3 1.4-.6 2 1.3 1.5-1.5-1.3-2 .6-1.4z"/></svg></span>
  </header>
  <div class="winner-body glow">
    <div class="winner-label">Winner</div>
    <div class="avatar" role="img" aria-label="Winner profile photo"></div>
    <div class="winner-name">Owen Hartley</div>
  </div>
</section>

</body>
</html>
```